Website - freeride bike clothing company

Need a complete website with eCommerce.
Company: A new brand of bike (freeride) clothing...not the lycra stuff!

I have a design concept I have put together in Illustrator (see screen shots attached and below is a link to drop box with the full file - it was too heavy to attach here). The drop box folder also has images to use in the demo site. Refer to:
1) Landing Page - front page with images
2) Website - each subsequent page
3) Images folder
4) Logo for the website
https://www.filecrate-share.net/sh/q82wpx7mk3tzb/H5Lr9aNbQe

The above is my vision. Any design tips/suggestions to make it better are welcome. I want it to be easy to use and navigate and it needs to look RAD!

I do actually have a word press version of this with the first page already set up - if this can help?
I would like it up and running in 2 weeks (??), if possible.

I need to be able to turn on and off pages as I like, add products easily, team members etc.

I need eCommerce set up:
1) Direct to the public with pricing, shopping cart, online payment, shipping etc.
2) Wholesaler login. Same structure as public but I would need to pre-approve and set up any wholesalers to access this section, and it has different pricing.
I want to be able to turn on/off either of the above, ie: I might only use one or the other at one time.

Inspiration sites:
http://www.quillmark.com/au/en/womens/
http://au.belwarden.com/home.php
www.tundrafolk.com

Site pages:
1) HOME - Landing Page

2) Gear
2a) Ladies / Mens / Other (each it's own page, same format, I can add new categories anytime)
2a(i) Item specific drill down

3) Crew
3a) Drill down per team member

4) Happenings
4a) News / Events
4b) Media
4c) Adventures
4d) Videos

5) Customer Service
5a) Policies / FAQ
5b) Size Chart
5c) Material
5d) Store Locator
5e) Contact

6) Shopping cart / check out and wholesaler login section

Target Market(s)

Extreme sports 25 - 40 year olds.
Men and women.
It is mostly a mens sport, but I am making womens gear too.

Industry/Entity Type

Clothing

Requirements
Must have
• Funky cool way to showcase my clothing products
Cool, simple yet professional look
Easily viewable photos of the product - easy to scroll between shots and to enlarge where needed.
Link to facebook and social media for the news sections, liking etc.
Crew section - link to that specific persons feed ie: on facebook/instagram

Pages:
1) Home Page

2) Gear
2a) Ladies / Mens / Other (same format pages - can add catagories as I like)
2ab) Item Specific Drill Down
2abc) Shopping Cart

3) Crew landing
3a) Crew Drill Down per person

4) Happenings
4a) News / Events / Media / Adventures / Videos

5) Customer Service
5a) Policies / FAQs
5ab) Size Chart
5abc) Material

6) Store Locator

7) Shopping Cart - both direct to public and a wholesale login section (I need to be able to grant people access and a login to the wholesale section)
Possibility to add promo codes to make things cheaper for specific people or sale time etc...

```html
<!DOCTYPE html>
<html lang="en">
<head>
<meta charset="utf-8">
<title>Ridgeworn — Freeride Clothing</title>
<link href="https://fonts.googleapis.com/css2?family=Source+Sans+3:wght@400;600;700&display=swap" rel="stylesheet">
<style>
:root{
  --topbar:#241a17;
  --ink:#3a3a3a;
  --muted:#555;
  --panel:#121212;
  --footer:#050505;
  --white:#ffffff;
  --news-title:#2c4a66;
  --line:#9a9a9a;
  --fb:#3b5998;
  --ig:#7f5545;
  --tw:#2a9ad8;
  --vm:#1ab7ea;
}
*{box-sizing:border-box;margin:0;padding:0}
html,body{width:685px;height:1200px;overflow:hidden;background:#fff}
body{position:relative;font-family:"Source Sans 3",Arial,sans-serif;color:var(--ink)}
a{color:inherit;text-decoration:none}

.topbar{position:absolute;left:0;top:0;width:685px;height:70px;background:var(--topbar)}
.brand{position:absolute;left:50px;top:21px;display:flex;align-items:center;gap:8px;color:var(--white);font-weight:700;font-size:24px;letter-spacing:.5px;line-height:28px}
.brand-dot{width:14px;height:14px;border-radius:50%;background:var(--white)}
.account{position:absolute;top:34px;color:var(--white);font-size:9.6px;line-height:12px;text-transform:uppercase}
.account.login{left:492px}
.account.cart{left:552px}

.mainnav{position:absolute;left:0;top:70px;width:685px;height:53px;background:#fff}
.mainnav ul{list-style:none;position:absolute;top:22px;left:0;font-size:9.6px;line-height:12px;color:#333;text-transform:uppercase}
.mainnav li{position:absolute;white-space:nowrap}
.search{position:absolute;left:487px;top:17px;width:148px;height:20px;border:1px solid #bbb;font-size:8.5px;color:#888;padding:4px 7px}
.search svg{position:absolute;right:5px;top:4px}

.hero{position:absolute;left:0;top:123px;width:685px;height:252px;overflow:hidden;
  background:linear-gradient(180deg,#6f8aa8 0%,#8a6f4e 8%,#9a7a52 22%,#4e5a2e 42%,#3f4d26 60%,#6b6a3c 78%,#8a7e4c 100%)}
.hero-caption{position:absolute;left:50px;top:185px;width:479px;height:42px;background:rgba(40,40,40,.6);color:#fff;font-size:13.6px;line-height:42px;padding:0 14px;text-transform:uppercase;white-space:nowrap;overflow:hidden}
.hero-dots{position:absolute;left:599px;top:236px;display:flex;gap:3px}
.hero-dots span{width:7px;height:7px;border-radius:50%;background:#ddd}
.hero-dots span:first-child{background:#999}

.tile{position:absolute;width:188px;height:142px;overflow:hidden}
.tile-photo{position:absolute;inset:0}
.tile-title{position:absolute;left:0;right:0;top:53px;text-align:center;color:#fff;font-size:14px;line-height:18px;text-transform:uppercase;white-space:nowrap;text-shadow:0 1px 2px rgba(0,0,0,.35)}
.tile-title::after{content:"";display:block;width:108px;height:1px;background:rgba(255,255,255,.8);margin:3px auto 0}
.info{position:absolute;width:188px;height:142px;background:var(--panel);color:#fff;padding:10px 13px}
.info h2{font-weight:400;font-size:12.8px;line-height:16px;text-align:center;text-transform:uppercase}
.info h2::after{content:"";display:block;width:95px;height:1px;background:#aaa;margin:4px auto 9px}
.info p{font-size:8.4px;line-height:14.4px}
.play{position:absolute;left:78px;top:49px}

.news{position:absolute;left:447px;top:731px;width:188px}
.news h2{font-weight:400;font-size:13.6px;line-height:18px;text-align:center;color:#222;padding:3px 0 6px;border-bottom:1px solid var(--line)}
.news-item{position:absolute;left:1px;width:188px}
.news-thumb{position:absolute;left:0;top:0;width:57px;height:38px}
.news-item h3{position:absolute;left:71px;top:-1px;font-size:8.4px;line-height:11px;font-weight:600;color:var(--news-title);white-space:nowrap}
.news-item p{position:absolute;left:71px;top:13px;width:118px;font-size:7.6px;line-height:13px;color:var(--muted)}

.footer{position:absolute;left:0;top:1070px;width:685px;height:130px;background:var(--footer);color:#fff}
.footer h4{position:absolute;top:16px;font-weight:400;font-size:11.2px;line-height:14px}
.footer ul{list-style:none;position:absolute;top:38px;font-size:8.4px;font-weight:400;line-height:17.6px;color:#eee}
.social{position:absolute;left:50px;top:44px;display:flex;gap:6px}
.social a{width:21px;height:21px;display:flex;align-items:center;justify-content:center}
.social a::after{content:"";width:6px;height:6px;border-radius:50%;background:#fff}
.social .fb{background:var(--fb)}
.social .ig{background:var(--ig)}
.social .tw{background:var(--tw)}
.social .vm{background:var(--vm)}
</style>
</head>
<body>

<header class="topbar">
  <div class="brand"><span class="brand-dot"></span>RIDGEWORN</div>
  <a class="account login" href="#">Login</a>
  <a class="account cart" href="#">View cart (0) items</a>
</header>

<nav class="mainnav">
  <ul>
    <li style="left:50px">Home</li>
    <li style="left:101px">Gear</li>
    <li style="left:149px">Crew</li>
    <li style="left:198px">Happenings</li>
    <li style="left:278px">Customer Service</li>
    <li style="left:384px">Cart / Checkout</li>
  </ul>
  <div class="search">Search..
    <svg width="9" height="9" viewBox="0 0 10 10"><circle cx="4" cy="4" r="3" fill="none" stroke="#999" stroke-width="1.3"/><line x1="6.2" y1="6.2" x2="9" y2="9" stroke="#999" stroke-width="1.3"/></svg>
  </div>
</nav>

<section class="hero" role="img" aria-label="Young rider in orange and blue jersey standing beside a downhill bike in front of sandstone cliffs">
  <div class="hero-caption">Pinecliff season opened this weekend and they have stepped</div>
  <div class="hero-dots"><span></span><span></span><span></span><span></span></div>
</section>

<div class="info" style="left:50px;top:400px">
  <h2>The Gear</h2>
  <p>Typi non habent claritatem insitam; est usus legentis in iis qui facit eorum claritatem. Inv estigationes demonstraverunt lectores lege re me lius quod ii legunt saepius. Claritas est etiam processus dynamicus, qui sequitur mi utationem consuetudium lectorum.</p>
</div>
<div class="tile" style="left:249px;top:400px">
  <div class="tile-photo" role="img" aria-label="Rider descending a dirt trail with misty mountains behind" style="background:linear-gradient(175deg,#a9adb0 0%,#8e9294 28%,#6b6b5a 48%,#7d6c55 70%,#8f7a5e 100%)"></div>
  <div class="tile-title">I love my bicycle</div>
</div>
<div class="tile" style="left:447px;top:400px">
  <div class="tile-photo" role="img" aria-label="Rider on an orange bike riding through a forest" style="background:linear-gradient(100deg,#2f2a1e 0%,#5a5036 30%,#6e6040 55%,#43392a 80%,#2c2519 100%)"></div>
  <div class="tile-title">Men´s range</div>
</div>

<div class="tile" style="left:50px;top:564px">
  <div class="tile-photo" role="img" aria-label="Smiling rider in a green hooded jacket holding a map" style="background:linear-gradient(180deg,#4f6238 0%,#3f7f62 40%,#3a9578 65%,#4a6b4c 100%)"></div>
  <div class="tile-title">Lucien Varde</div>
</div>
<div class="tile" style="left:249px;top:564px">
  <div class="tile-photo" role="img" aria-label="Downhill racer riding through dense green bush" style="background:linear-gradient(160deg,#22381f 0%,#3f5e35 40%,#4a6a3a 60%,#24361f 100%)"></div>
  <div class="tile-title">Events</div>
</div>
<div class="tile" style="left:447px;top:564px">
  <div class="tile-photo" role="img" aria-label="Female rider in a checked jersey and helmet on a road" style="background:linear-gradient(180deg,#6f7a58 0%,#75786a 35%,#5d5d66 60%,#4a4760 100%)"></div>
  <div class="tile-title">Ladies range</div>
</div>

<div class="tile" style="left:50px;top:731px">
  <div class="tile-photo" role="img" aria-label="Female rider seen from behind wearing a purple checked jersey in a village street" style="background:linear-gradient(180deg,#6e7a6a 0%,#6c6a6e 40%,#534f82 70%,#463c86 100%)"></div>
  <div class="tile-title">Rowan Eddis</div>
</div>
<div class="tile" style="left:249px;top:731px">
  <div class="tile-photo" role="img" aria-label="Video still of riders in team jerseys at an event podium" style="background:linear-gradient(100deg,#2e2a28 0%,#4a4442 30%,#7a7478 55%,#5a5468 80%,#3e3a44 100%)"></div>
  <svg class="play" width="34" height="34" viewBox="0 0 34 34"><circle cx="17" cy="17" r="16" fill="#000" stroke="#fff" stroke-width="2"/><polygon points="13,10 25,17 13,24" fill="#fff"/></svg>
</div>

<div class="info" style="left:50px;top:898px">
  <h2>The Team</h2>
  <p>Typi non habent claritatem insitam; est usus legentis in iis qui facit eorum claritatem. Inv estigationes demonstraverunt lectores lege re me lius quod ii legunt saepius. Claritas est etiam processus dynamicus, qui sequitur mi utationem consuetudium lectorum.</p>
</div>
<div class="tile" style="left:249px;top:898px">
  <div class="tile-photo" role="img" aria-label="Close-up of a helmeted rider in an orange and blue jersey" style="background:linear-gradient(135deg,#5e5248 0%,#8a5e3c 35%,#a0602f 55%,#5a5a6e 80%,#4a4a58 100%)"></div>
  <div class="tile-title">Corbin Hale</div>
</div>

<aside class="news">
  <h2>NEWS</h2>
  <div class="news-item" style="top:44px">
    <div class="news-thumb" role="img" aria-label="Rider on a wooded trail" style="background:linear-gradient(160deg,#4a6a2a,#8a7a3a)"></div>
    <h3>Breathing Life Into Fitness!</h3>
    <p>Marisol craves the endorphin rush fueled by fitness and uses it.</p>
  </div>
  <div class="news-item" style="top:95px">
    <div class="news-thumb" role="img" aria-label="Rider in green jacket outdoors" style="background:linear-gradient(160deg,#4a5a3a,#3f7a5a)"></div>
    <h3>Breathing Life Into Fitness!</h3>
    <p>Marisol craves the endorphin rush fueled by fitness and uses it.</p>
  </div>
  <div class="news-item" style="top:149px">
    <div class="news-thumb" role="img" aria-label="Group of riders at an event" style="background:linear-gradient(160deg,#6a6a5a,#5a5060)"></div>
    <h3>Breathing Life Into Fitness!</h3>
    <p>Marisol craves the endorphin rush fueled by fitness and uses it.</p>
  </div>
  <div class="news-item" style="top:203px">
    <div class="news-thumb" role="img" aria-label="Race crowd under event flags" style="background:linear-gradient(160deg,#7a7a7a,#5a4a4a)"></div>
    <h3>Breathing Life Into Fitness!</h3>
    <p>Marisol craves the endorphin rush fueled by fitness and uses it.</p>
  </div>
  <div class="news-item" style="top:258px">
    <div class="news-thumb" role="img" aria-label="Rider on a grassy downhill slope" style="background:linear-gradient(160deg,#6a7a5a,#8a9070)"></div>
    <h3>Breathing Life Into Fitness!</h3>
    <p>Marisol craves the endorphin rush fueled by fitness and uses it. Clarita est etiam processus dynamicus</p>
  </div>
</aside>

<footer class="footer">
  <h4 style="left:50px">Socialise</h4>
  <div class="social">
    <a class="fb" href="#" aria-label="Social page one"></a>
    <a class="ig" href="#" aria-label="Social page two"></a>
    <a class="tw" href="#" aria-label="Social page three"></a>
    <a class="vm" href="#" aria-label="Social page four"></a>
  </div>
  <h4 style="left:254px">Gear</h4>
  <ul style="left:254px"><li>Ladies</li><li>Men</li><li>Gravity</li><li>Trail</li></ul>
  <h4 style="left:344px">Customer Service</h4>
  <ul style="left:344px"><li>Size Chart</li><li>Fabric Details</li><li>Policies</li><li>Contact</li></ul>
  <h4 style="left:480px">Happenings</h4>
  <ul style="left:480px"><li>Team</li><li>Events</li><li>Adventure</li><li>Moofe</li></ul>
</footer>

</body>
</html>
```